BHAG Poster

We like creativity and visual boxes and shapes not just bullet points. We think we want it to be landscape view. Here are some of the parameters:

BHAG:
Become one of the most admired construction companies in the markets we serve within the next 10 years

3 – 5 year goals:
1. Generate 35m in revenue by 2020
2. Have a 50/50 mix of Public-Private job mix
3. Maintain 15% annual growth

1 year goals:
1. $24M in revenue with better margins
2. 14% gross margin on year
3. Business development begins to pay off
4. Continue recruiting great & talented people

Dynamic Quarter Goal:
(Leave this area blank so we can fill it in each quarter please)

Industry/Entity Type

Landscape

Colors
0355a3

Requirements
Must have
• SHAPES OR BOXES FOR VISUAL EFFECT. We don't want it to just be words on a page. Must be creative. Must have our logo somewhere on the poster. Our cmyk blue color is 100-80-0-22. Poster can have different colors, but it just needs to have some of our blue in it.
Should not have
• no bullet points

```html
<!DOCTYPE html>
<html lang="en">
<head>
<meta charset="utf-8">
<title>Harlan Construction – BHAG Poster</title>
<link href="https://fonts.googleapis.com/css2?family=Barlow+Condensed:wght@600;700&family=Exo+2:wght@500;600&family=Lato:wght@400;700&display=swap" rel="stylesheet">
<style>
  :root{
    --brand-blue:#0355a3;
    --navy:#263a85;
    --navy-deep:#1f2f72;
    --sky:#3fb9e6;
    --charcoal:#474749;
    --charcoal-dark:#3b3b3d;
    --ink:#1d1d1f;
    --heading-grey:#3c3c3e;
    --paper:#ffffff;
    --mist:#eeeff2;
    --stage:#d9d9db;
  }
  *{box-sizing:border-box;margin:0;padding:0}
  html,body{width:1200px;height:1097px;overflow:hidden;background:var(--stage)}
  .poster{position:absolute;left:20px;top:98px;width:1160px;height:900px;background:var(--mist);overflow:hidden;box-shadow:0 6px 18px rgba(0,0,0,.25)}
  .header{position:absolute;left:0;top:0;width:843px;height:160px;background:var(--paper)}
  .header-side{position:absolute;left:843px;top:0;width:317px;height:160px;background:var(--charcoal)}
  .brand{position:absolute;left:46px;top:56px;display:flex;align-items:center;gap:10px}
  .brand-mark{width:56px;height:56px;background:var(--navy-deep)}
  .brand-name{font:700 34px/0.95 "Barlow Condensed",sans-serif;color:var(--navy-deep);letter-spacing:.5px}
  .tagline{position:absolute;left:356px;top:34px;font:700 48px/1 "Barlow Condensed",sans-serif;letter-spacing:1.5px}
  .tagline .line-1{color:var(--heading-grey);display:block}
  .tagline .line-2{color:var(--navy);display:block;margin-top:4px}
  .rule{position:absolute;left:0;width:1160px;height:6px;background:var(--navy)}
  .rule-top{top:162px}
  .rule-bottom{top:477px}
  .hero{position:absolute;left:0;top:174px;width:1160px;height:298px;background:linear-gradient(180deg,#9fc4df 0%,#5f8db5 45%,#3a6690 100%)}
  .lower{position:absolute;left:0;top:485px;width:843px;height:335px;background:linear-gradient(180deg,#e9eaee,#f5f5f7)}
  .goals{position:absolute;left:44px;top:564px;width:738px;height:210px;border-radius:10px;background:linear-gradient(180deg,#2e4590,var(--navy-deep));display:flex;color:var(--paper)}
  .goal-col{position:relative;padding:38px 0 0 24px}
  .goal-col.long{width:366px;border-right:1px solid rgba(255,255,255,.2)}
  .goal-col.short{flex:1;padding-left:20px}
  .goal-title{font:500 28px/1 "Exo 2",sans-serif;color:var(--sky);margin-bottom:14px}
  .goal-list{list-style:none;font:400 16px/1 "Lato",sans-serif}
  .goal-list li{display:flex;align-items:center;gap:12px;height:28px;margin-bottom:6px}
  .goal-col.short .goal-list li{margin-bottom:1px}
  .goal-list svg{flex:none}
  .badge{position:absolute;width:78px;height:78px;border-radius:50%;background:var(--navy-deep);border:4px solid #dfe3ee;display:flex;align-items:center;justify-content:center;box-shadow:0 0 0 2px var(--navy-deep)}
  .bhag{position:absolute;left:843px;top:485px;width:317px;height:158px;background:var(--charcoal);padding:34px 32px 0 26px;color:var(--paper)}
  .bhag-title{font:600 24px/1 "Exo 2",sans-serif;color:var(--sky);margin-bottom:20px}
  .bhag-text{font:400 14.5px/1.25 "Lato",sans-serif;text-align:justify}
  .quarter{position:absolute;left:824px;top:643px;width:336px;height:177px;background:linear-gradient(90deg,#d3d3d6,#ffffff 22%,#ffffff);padding:24px 28px 0 44px}
  .quarter-head{display:flex;align-items:center;gap:14px;margin-bottom:12px}
  .quarter-icon{width:44px;height:44px;border-radius:50%;background:var(--navy-deep);border:3px solid #fff;box-shadow:0 0 0 2px var(--navy-deep);display:flex;align-items:center;justify-content:center}
  .quarter-title{font:600 24px/1.15 "Barlow Condensed",sans-serif;color:var(--navy-deep);letter-spacing:.5px}
  .quarter-text{font:400 14.5px/1.12 "Lato",sans-serif;color:var(--ink)}
  .footer{position:absolute;left:0;top:820px;width:1160px;height:61px;background:var(--charcoal-dark);display:flex;align-items:center;gap:18px;padding-left:44px;color:var(--paper);font:400 13.5px/1 "Lato",sans-serif}
  .footer .item{display:flex;align-items:center;gap:10px}
  .footer-band{position:absolute;left:0;top:881px;width:1160px;height:19px;background:var(--paper)}
  .footer-band::after{content:"";position:absolute;left:0;top:5px;width:100%;height:14px;background:var(--navy)}
</style>
</head>
<body>
<main class="poster">
  <header class="header">
    <div class="brand">
      <span class="brand-mark"></span>
      <span class="brand-name">HARLAN<br>CONSTRUCTION</span>
    </div>
    <h1 class="tagline"><span class="line-1">QUALITY CONSTRUCTION</span><span class="line-2">FIRST CLASS DELIVERY</span></h1>
  </header>
  <div class="header-side"></div>
  <div class="rule rule-top"></div>
  <div class="hero" role="img" aria-label="Blue-toned photo of a crew and excavators working on a downtown street"></div>
  <div class="rule rule-bottom"></div>

  <section class="lower">
  </section>

  <section class="goals">
    <div class="goal-col long">
      <h2 class="goal-title">3 – 5 YEAR GOALS:</h2>
      <ul class="goal-list">
        <li><svg width="20" height="16" viewBox="0 0 20 16"><rect x="1" y="9" width="3" height="7" fill="#bcd3f0"/><rect x="7" y="6" width="3" height="10" fill="#bcd3f0"/><rect x="13" y="3" width="3" height="13" fill="#bcd3f0"/></svg>Generate 35m in revenue by 2020</li>
        <li><svg width="20" height="18" viewBox="0 0 20 18"><circle cx="6" cy="4" r="3" fill="#bcd3f0"/><circle cx="14" cy="4" r="3" fill="#bcd3f0"/><rect x="3" y="8" width="6" height="10" fill="#bcd3f0"/><rect x="11" y="8" width="6" height="10" fill="#bcd3f0"/></svg>Have a 50/50 mix of Public-Private job mix</li>
        <li><svg width="20" height="16" viewBox="0 0 20 16"><rect x="1" y="9" width="3" height="7" fill="#bcd3f0"/><rect x="7" y="6" width="3" height="10" fill="#bcd3f0"/><rect x="13" y="3" width="3" height="13" fill="#bcd3f0"/></svg>Maintain 15% annual growth</li>
      </ul>
      <div class="badge" style="left:112px;top:-92px"><svg width="34" height="34" viewBox="0 0 34 34"><path d="M17 4 L27 16 H21 V29 H13 V16 H7 Z" fill="#fff"/></svg></div>
    </div>
    <div class="goal-col short">
      <h2 class="goal-title">1 YEAR GOALS:</h2>
      <ul class="goal-list">
        <li><svg width="18" height="16" viewBox="0 0 18 16"><circle cx="7" cy="5" r="4" fill="#bcd3f0"/><path d="M1 15 Q7 8 13 15 Z" fill="#bcd3f0"/></svg>$24M in revenue with better margins</li>
        <li><svg width="18" height="16" viewBox="0 0 18 16"><circle cx="7" cy="5" r="4" fill="#bcd3f0"/><path d="M1 15 Q7 8 13 15 Z" fill="#bcd3f0"/></svg>14% gross margin on year</li>
        <li><svg width="18" height="18" viewBox="0 0 18 18"><circle cx="9" cy="9" r="8" fill="#bcd3f0"/><path d="M9 9 V1 A8 8 0 0 1 17 9 Z" fill="#fff"/></svg>Business development begins to pay off</li>
        <li><svg width="18" height="18" viewBox="0 0 18 18"><path d="M3 9 A6 6 0 0 1 14 5" stroke="#bcd3f0" stroke-width="2.4" fill="none"/><path d="M15 9 A6 6 0 0 1 4 13" stroke="#bcd3f0" stroke-width="2.4" fill="none"/><path d="M11 2 L16 5 L12 8 Z" fill="#bcd3f0"/><path d="M7 16 L2 13 L6 10 Z" fill="#bcd3f0"/></svg>Continue recruiting great &amp; talented people</li>
      </ul>
      <div class="badge" style="left:110px;top:-92px"><svg width="34" height="34" viewBox="0 0 34 34"><path d="M17 4 L27 16 H21 V29 H13 V16 H7 Z" fill="#fff"/></svg></div>
    </div>
  </section>

  <aside class="bhag">
    <h2 class="bhag-title">BHAG:</h2>
    <p class="bhag-text">Become one of the most admired construction companies in the markets we serve within the next 10 years</p>
  </aside>

  <aside class="quarter">
    <div class="quarter-head">
      <span class="quarter-icon"><svg width="20" height="20" viewBox="0 0 34 34"><path d="M17 4 L27 16 H21 V29 H13 V16 H7 Z" fill="#fff"/></svg></span>
      <h2 class="quarter-title">DYNAMIC<br>QUARTER GOAL:</h2>
    </div>
    <p class="quarter-text">Lorem Ipsum is simply dummy text of the printing and typesetting industry Lorem Ipsum is simply dummy text of the printing and typesetting industry</p>
  </aside>

  <footer class="footer">
    <span class="item"><svg width="22" height="18" viewBox="0 0 22 18"><path d="M11 1 L21 9 H18 V17 H13 V12 H9 V17 H4 V9 H1 Z" fill="#fff"/></svg>820 Foundry Lane Riverton, Ohio 44102</span>
    <span class="item"><svg width="18" height="18" viewBox="0 0 18 18" fill="none" stroke="#fff" stroke-width="1.5"><circle cx="9" cy="9" r="7.5"/><ellipse cx="9" cy="9" rx="3.5" ry="7.5"/><path d="M1.5 9 H16.5 M3 5 H15 M3 13 H15"/></svg>www.harlanbuilds.com</span>
    <span class="item"><svg width="20" height="20" viewBox="0 0 20 20"><path d="M4 2 L8 6 L6 8 Q8 12 12 14 L14 12 L18 16 L15 19 Q6 17 1 5 Z" fill="#fff"/></svg>555-204-7183</span>
  </footer>
  <div class="footer-band"></div>
</main>
</body>
</html>
```